Flyer for an pediatric sleep consultancy - to distribute to play and childcare centers etc.

I need a flyer that will attract the attention of parents with children between the age of babies to toddlers, who may be experiencing sleep issues. The flyer will be placed at places such as community centers, doctors room, play centers, kindergardens, etc.

My company is called "The Quiet Meadow Studio" and provides a sleep consultancy service. My service essentially provides a customized plan for parents to follow and general advice and guidance. It is not medical advice.

I like to the flyer to have an overall tone that is soft and peaceful with a clean and beautiful design, however can catch the attention of parents who may be struggling with their child's sleep issues and are sleep deprived. I would like photos with minimal text. The colour I use is a brownish rose. I will attach some of my designs to give you an idea. You can have a look at my homepage as well to get an idea about my esthetic direction and the colour. Although the colour of my page is a bit too brownish....

I will provide the text to appear in the flyer once I have a better idea of the layout that I prefer for the flyer. The text however wont be extensive, just some catchy points.

I want to direct people to my website which is www.quietmeadowstudio-example.com
I offer a first FREE evaluation call, to the parents, to get to know each other better, learn about their child's particular sleep problems and see if we are a good fit and can work together. I would like to have this information somehow on the flyer, so that the parents will contact me.
I also have a FriendWall page, which is: The Quiet Meadow Studio

I have a logo that I would like to appear on the flyer. I will attach the file once the uploader on art bazaar is fixed.

When I print the flyer - I like to print A5 SIZE ... please make sure the formatting is OK for this size.

Here are some text ideas. of course all of it would be too much, I guess. On the front of the flyer I would like to have some catchy phrase or something similar to get people interested and to want to know more. On the back there could be a bit more text and information. But I'm open too suggestions....
I'm not too sure about the wording yet. But here are some text that I might be use:

Is sleep an issue in your home?

Is your baby having trouble sleeping? ... are you?!
I can help!

Sleep, baby, sleep….

Teaching children how to sleep

The Quiet Meadow Studio is a pediatric sleep consultancy that specializes in helping parents with children who struggle to develop good and healthy sleep habits.
Disruptive sleep patterns or not enough sleep can affect the physical, mental and emotional development of your child.

Of course nobody plans to have a sleep problem, but habits can become easily ingrained and spiral quickly out of control and you can find yourself sleep deprived, desperate and not too sure what to do. You see all the other sleeping babies and wish there was someone who understood what you were going through?! Well, there is!

Contact me for a free 15 minute consultation.

This 15 minute „mini“ consultation is a chance to discuss your unique sleep challenges and sleep goals with me. I will provide you with an overview of how I will work with your family to achieve your wildest sleep dreams (goals).
Furthermore do I understand and believe that every child and their family is unique and there is no one size fits all!
I would love to have a chat with you and talk about how I can help make things easier for you and your family!

Do I need a sleep consultant for my child?
The answer is yes if:
- if your child will only fall asleep when nursing or bottle feeding
- if your child needs a dummy or other external aid, like being rocked, patted or taken for a care ride to fall asleep
- if your good night routine is a challenging and exhausting procedure instead of a relaxed and enjoyable moment for the whole family
- if sleep is a constant battle in your home which leaves you feeling frustrated and exhausted
- if your own lack of sleep is taking a toll on you and the whole family

What can I do for you?

I will:

- Guide you to set an age appropriate foundation for good sleep
- Create an individual sleep plan tailored especially to your child’s sleep needs and circumstances
- Help you to teach your childto go to sleep and get back to sleep independently during the night
- show you how to teach your child to take healthful, restorative naps
-Learn

Contact:

Marta Lindqvist
info@quietmeadowstudio-example.com
www.quietmeadowstudio-example.com
+34 612 380 574

Consultations in English, German or Spanish via Phone/VoxCall or home consultation

Reason: I have to go on a business trip and won't be able to choose a design until the deadline. During the trip I won't have time to give feedback and ask for changes. thank you

Target Market(s)

parents, sleep deprived mothers, young families, child care provider,

Industry/Entity Type

Baby Care

Contact Information for Business Card

Marta Lindqvist
pediatric sleep consultant
+34 612 380 574

```html
<!DOCTYPE html>
<html lang="en">
<head>
<meta charset="utf-8">
<title>The Quiet Meadow Studio – Flyer Front and Back</title>
<link href="https://fonts.googleapis.com/css2?family=Rokkitt:wght@300;400&family=Oswald:wght@400;500&family=Source+Sans+3:ital,wght@0,400;0,600;1,400&family=Raleway:wght@300;400&family=Signika:wght@400&display=swap" rel="stylesheet">
<style>
  :root{
    --rose:#c47b6d;
    --rose-soft:#e2a79c;
    --sage:#7f948a;
    --sage-dark:#5d7469;
    --mist:#e8ecea;
    --ink:#2b2b2b;
    --grey:#8a8a8a;
    --paper:#ffffff;
    --stage:#e6e6e6;
  }
  *{box-sizing:border-box;margin:0;padding:0}
  html,body{width:1200px;height:1200px;overflow:hidden;background:var(--stage)}
  .canvas{position:relative;width:1200px;height:1200px}
  .flyer{position:absolute;top:275px;width:465px;height:650px;background:var(--paper);overflow:hidden;font-family:"Source Sans 3",sans-serif;color:var(--ink)}
  .flyer--front{left:105px}
  .flyer--back{left:629px}
  .abs{position:absolute}
  svg.abs{display:block}

  /* front */
  .hero-photo{left:140px;top:0;width:325px;height:262px;background:radial-gradient(ellipse at 60% 45%,#f3d2c0 0%,#f4e2d8 45%,#f7eeea 70%,rgba(255,255,255,0) 100%)}
  .headline{left:32px;top:44px;font-family:"Rokkitt",serif;font-weight:400;font-size:35px;line-height:37px;color:var(--rose)}
  .headline .last{color:var(--sage-dark)}
  .brand{font-family:"Raleway",sans-serif;font-weight:300;color:var(--grey);white-space:nowrap}
  .brand-front{left:22px;top:262px;font-size:14px;display:flex;align-items:center;gap:6px}
  .brand-dot{width:9px;height:9px;border-radius:50%;background:var(--rose-soft);display:inline-block}
  .badge{left:269px;top:218px;width:172px;height:172px;border-radius:50%;background:var(--rose);border:5px solid #fff;box-shadow:0 0 0 2px #e9d2cc,0 3px 8px rgba(0,0,0,.15);color:#fff;text-align:center;font-family:"Oswald",sans-serif}
  .badge .free{font-size:48px;font-weight:500;line-height:1;margin-top:28px;letter-spacing:1px}
  .badge .call{font-size:23px;font-weight:400;line-height:1;margin-top:6px}
  .kicker{left:39px;top:350px;font-family:"Rokkitt",serif;font-size:14px;color:var(--sage-dark);letter-spacing:.5px}
  .title{left:39px;top:364px;font-family:"Rokkitt",serif;font-weight:300;font-size:26px;color:var(--rose);letter-spacing:.5px}
  .intro{left:39px;top:398px;width:392px;font-size:11px;line-height:13px}
  .intro p+p{margin-top:4px}
  .portrait{left:258px;top:460px;width:176px;height:176px;border-radius:50%;background:radial-gradient(circle at 50% 45%,#d9d2cf 0%,#eeeae8 60%,#f7f5f4 100%);border:4px solid #fff;box-shadow:0 0 0 2px #dcdcdc}
  .ask{left:39px;top:532px;width:200px;font-family:"Rokkitt",serif;font-size:11px;line-height:12px;color:var(--sage-dark)}
  .ask-body{left:39px;top:556px;width:196px;font-size:9.5px;line-height:11.5px;text-align:justify}
  .follow{left:39px;top:614px;font-size:8px;color:var(--sage-dark);display:flex;align-items:center;gap:5px}
  .follow .dot{width:13px;height:13px;border-radius:50%;background:var(--sage-dark)}

  /* back */
  .brand-back{left:0;width:465px;top:60px;font-size:16px;text-align:center;display:flex;justify-content:center;align-items:center;gap:7px}
  .pill{left:36px;top:105px;width:403px;height:31px;border-radius:16px;background:var(--rose);color:#fff;font-family:"Signika",sans-serif;font-size:18px;line-height:31px;text-align:center}
  .lead{left:24px;top:143px;width:418px;font-size:8px;line-height:10.2px;text-align:justify}
  .panel{left:0;top:193px;width:465px;height:290px;background:var(--mist)}
  .divider{left:231px;top:200px;width:1px;height:200px;background:#fff}
  .col{top:200px;font-size:7.3px;line-height:9.5px}
  .col-left{left:33px;width:194px}
  .col-right{left:257px;width:186px}
  .col h3{font-family:"Source Sans 3",sans-serif;font-weight:400;font-size:10.5px;line-height:12.5px;color:var(--sage-dark)}
  .col .sub{font-style:italic;font-size:9.5px;color:var(--sage);margin:3px 0 4px}
  .col ul{list-style:none}
  .col li{font-style:italic;position:relative;padding-left:7px;margin-bottom:4.4px;text-align:justify}
  .col li::before{content:"";position:absolute;left:0;top:3px;width:3px;height:3px;border-radius:50%;background:var(--rose)}
  .snap{border-radius:50%;border:4px solid #fff;box-shadow:0 0 0 2px var(--sage)}
  .snap-a{left:84px;top:440px;width:86px;height:86px;background:radial-gradient(circle,#f2c9b8,#f6e3da)}
  .snap-b{left:179px;top:421px;width:106px;height:106px;background:radial-gradient(circle,#f3d6c7,#f4ece7)}
  .snap-c{left:281px;top:440px;width:86px;height:86px;background:radial-gradient(circle,#f1d0bf,#f8f0eb)}
  .visit{left:0;width:465px;top:543px;text-align:center;font-size:7.8px;line-height:10.5px}
  .visit .hl{color:var(--rose)}
  .visit .guide{color:var(--rose);font-style:italic}
  .visit .langs{color:var(--sage-dark)}
  .contact-title{left:0;width:465px;top:596px;text-align:center;font-family:"Raleway",sans-serif;font-size:15px;color:var(--rose)}
  .contact-title span{color:var(--ink)}
  .contact-line{left:0;width:465px;top:618px;display:flex;justify-content:center;gap:14px;font-size:7.6px}
  .contact-line span{display:flex;align-items:center;gap:4px}
</style>
</head>
<body>
<div class="canvas">

  <!-- Front -->
  <section class="flyer flyer--front">
    <div class="abs hero-photo" role="img" aria-label="Photo of a mother resting her cheek against her sleeping baby"></div>
    <h1 class="abs headline">Sleep,<br>Baby,<br><span class="last">Sleep....</span></h1>

    <svg class="abs" style="left:0;top:0" width="465" height="650" viewBox="0 0 465 650">
      <path d="M0 232 C90 210 200 205 300 230 C360 245 420 262 465 258 L465 268 C410 270 360 254 300 242 C200 220 90 228 0 245 Z" fill="var(--sage)"/>
      <path d="M0 245 C90 228 200 220 300 242 C360 254 410 270 465 268 L465 650 L0 650 Z" fill="#fff"/>
      <path d="M0 312 C120 318 220 305 300 290 C360 278 420 282 465 290 L465 296 C420 290 360 288 300 300 C220 316 110 330 0 326 Z" fill="var(--rose-soft)"/>
      <path d="M0 530 C80 505 180 500 260 518 C330 534 400 540 465 522 L465 527 C400 548 330 542 260 528 C180 510 80 515 0 540 Z" fill="var(--rose-soft)"/>
    </svg>

    <div class="abs brand brand-front"><span class="brand-dot"></span>The Quiet Meadow Studio</div>

    <div class="abs badge">
      <div class="free">FREE</div>
      <div class="call">Evaluation Call</div>
    </div>

    <div class="abs kicker">TEACHING CHILDREN</div>
    <h2 class="abs title">HOW TO SLEEP</h2>
    <div class="abs intro">
      <p>The Quiet Meadow Studio is a pediatric sleep consultancy that specializes in helping parents with children who struggle to develop good and healthy sleep habits.</p>
      <p>Disruptive sleep patterns or not enough sleep can affect the physical, mental and emotional development of your child.</p>
    </div>

    <div class="abs portrait" role="img" aria-label="Photo of the sleep consultant holding a smiling toddler"></div>

    <div class="abs ask">Is your baby having trouble sleeping?<br>... are you?!</div>
    <div class="abs ask-body">You see all the other sleeping babies and wish there was someone who understood what you were going through?! Well, there is!<br>I can help!</div>
    <div class="abs follow"><span class="dot"></span>Follow Us on our FriendWall page</div>
  </section>

  <!-- Back -->
  <section class="flyer flyer--back">
    <div class="abs brand brand-back"><span class="brand-dot"></span>The Quiet Meadow Studio</div>
    <div class="abs pill">Contact me for a free 15 minute consultation</div>
    <p class="abs lead">This 15 minute „mini“ consultation is a chance to discuss your unique sleep challenges and sleep goals with me. I will provide you with an overview of how I will work with your family to achieve your wildest sleep dreams (goals). Furthermore do I understand and believe that every child and their family is unique and there is no one size fits all! I would love to have a chat with you and talk about how I can help make things easier for you and your family!</p>

    <div class="abs panel"></div>
    <svg class="abs" style="left:0;top:440px" width="465" height="50" viewBox="0 0 465 50">
      <path d="M0 28 C70 8 150 4 232 12 C320 20 400 10 465 30 L465 50 L0 50 Z" fill="var(--rose-soft)"/>
      <path d="M0 40 C70 22 150 18 232 26 C320 34 400 26 465 42 L465 50 L0 50 Z" fill="#fff"/>
    </svg>
    <div class="abs divider"></div>

    <div class="abs col col-left">
      <h3>Do I need a sleep consultant<br>for my child?</h3>
      <p class="sub">The answer is yes if:</p>
      <ul>
        <li>If your child will only fall asleep when nursing or bottle feeding</li>
        <li>If your child needs a dummy or other external aid, like being rocked, patted or taken for a care ride to fall asleep</li>
        <li>If your child wakes up at night or too early in the morning and needs help or assistance to go back to sleep</li>
        <li>If your good night routine is a challenging and exhausting procedure instead of a relaxed and enjoyable moment for the whole family</li>
        <li>If naps are a disaster or it is hard to establish a good schedule</li>
        <li>If sleep is a constant battle in your home which leaves you feeling frustrated and exhausted</li>
        <li>If your own lack of sleep is taking a toll on you and the whole family</li>
      </ul>
    </div>

    <div class="abs col col-right">
      <h3>What can I do for you?</h3>
      <p class="sub">I will</p>
      <ul>
        <li>Guide you to set an age appropriate foundation for good sleep</li>
        <li>Create an individual sleep plan tailored especially to your child's sleep needs and circumstances</li>
        <li>Help you to teach your child to go to sleep and get back to sleep independently during the night in order to sleep through</li>
        <li>Establish together with you a good eat/sleep schedule for your child</li>
        <li>Show you how to teach your child to take healthful, restorative naps</li>
        <li>Give you the tools to overcome any sleep obstacle or roadblock you might encounter in the future</li>
        <li>Be by your side during the whole process to guide, motivate and comfort you</li>
      </ul>
    </div>

    <div class="abs snap snap-a" role="img" aria-label="Photo of a baby's tiny hand in a parent's hand"></div>
    <div class="abs snap snap-b" role="img" aria-label="Photo of two young children asleep side by side"></div>
    <div class="abs snap snap-c" role="img" aria-label="Photo of a toddler sleeping on a white pillow"></div>

    <div class="abs visit">
      Visit my website and download your <span class="hl">FREE</span> guide:<br>
      <span class="guide">"The six steps to help your baby sleep through the night"</span> or book your <span class="hl">FREE</span> evaluation call.<br>
      <span class="langs">Consultations in English, German or Spanish via Phone/VoxCall or home consultation</span>
    </div>

    <div class="abs contact-title">Contact Us: <span>Marta Lindqvist</span></div>
    <div class="abs contact-line">
      <span><svg width="8" height="8" viewBox="0 0 10 10"><path d="M2 1 L4 1 L4.6 3.2 L3.4 4.2 C4 5.4 4.8 6.2 6 6.8 L7 5.6 L9 6.2 L9 8.2 C9 8.8 8.5 9.2 8 9.1 C4.5 8.6 1.6 5.8 1 2.1 C0.9 1.5 1.4 1 2 1 Z" fill="var(--rose)"/></svg>+34 612 380 574</span>
      <span><svg width="9" height="7" viewBox="0 0 10 8"><rect x="0.5" y="0.5" width="9" height="7" fill="none" stroke="var(--rose)"/><path d="M0.5 0.5 L5 4.5 L9.5 0.5" fill="none" stroke="var(--rose)"/></svg>info@quietmeadowstudio-example.com</span>
      <span><svg width="8" height="8" viewBox="0 0 10 10"><circle cx="5" cy="5" r="4.3" fill="none" stroke="var(--rose)"/><path d="M0.7 5 H9.3 M5 0.7 C3 3 3 7 5 9.3 M5 0.7 C7 3 7 7 5 9.3" fill="none" stroke="var(--rose)" stroke-width=".8"/></svg>www.quietmeadowstudio-example.com</span>
    </div>
  </section>

</div>
</body>
</html>
```